Managed Service Provider email

We need an email designed that advertises our Managed Services product. We have been in business 28 years. Managed Services includes proactive ticketing, Help desk support, server and workstation monitoring, data backup monitoring, spam protection, regular reports, Deskflow 240, telecom services, ISP management, vendor management and more.

Target Market(s)

Business owners, decision makers, IT, CTO

Industry/Entity Type

Information Technology

Colors

Designer to choose colors to be used in the design.

Requirements
Must have
• Bullet points with included services. Mention of 28 years in business.
Nice to have
• We'd love our designer to read up on what an MSP (Managed Service Provider) does and use that information to find/create content for our email project.
Should not have
• A picture of a computer with a thermometer in its mouth.

```html
<!DOCTYPE html>
<html lang="en">
<head>
<meta charset="utf-8">
<title>Velto Network Services – Managed Services Email</title>
<link rel="stylesheet" href="https://fonts.googleapis.com/css2?family=Open+Sans:wght@400;600;700;800&family=Arimo:wght@400;700&display=swap">
<style>
:root{
  --ink:#3a3f45;
  --ink-soft:#5b5f63;
  --blue:#2f8fde;
  --blue-panel:#4da4e6;
  --btn-blue:#1a7fe0;
  --white:#ffffff;
  --band:#f3f2f3;
  --footer:#3c4148;
  --bg-teal:#2a8f9c;
  --bg-deep:#175f72;
  --bg-glow:#dfe6a6;
}
*{margin:0;padding:0;box-sizing:border-box}
html,body{width:1200px;height:2473px;overflow:hidden}
body{
  position:relative;
  font-family:"Open Sans",Arial,sans-serif;
  color:var(--ink);
  background:
    radial-gradient(ellipse 620px 420px at 600px 120px,var(--bg-glow) 0%,rgba(170,220,190,.7) 40%,rgba(90,190,190,0) 100%),
    radial-gradient(ellipse 900px 1600px at 600px 900px,#5fc2c4 0%,var(--bg-teal) 50%,var(--bg-deep) 100%);
}
.abs{position:absolute}

/* presentation header */
.board-title{left:0;width:1200px;top:46px;text-align:center;font-weight:800;font-size:32px;letter-spacing:.5px;text-decoration:underline;text-underline-offset:5px;color:var(--ink)}
.board-brand{left:222px;top:150px;font-weight:700;color:var(--ink);line-height:1}
.board-brand .name{font-size:72px;letter-spacing:2px}
.board-brand .sub{font-size:27px;margin-top:6px;letter-spacing:1px}
.features{left:615px;top:116px;list-style:none}
.features li{font-weight:700;font-size:24px;line-height:41px;color:var(--ink);position:relative;padding-left:26px}
.features li::before{content:"";position:absolute;left:0;top:16px;width:9px;height:9px;background:var(--blue)}

/* email card */
.email{left:185px;top:328px;width:820px;height:2124px;background:var(--white);box-shadow:0 0 6px rgba(0,0,0,.25);overflow:hidden}
.email-brand{left:0;top:45px;width:820px;text-align:center;font-weight:700;color:var(--ink);line-height:1}
.email-brand .name{font-size:66px;letter-spacing:2px}
.email-brand .sub{font-size:26px;margin-top:6px;letter-spacing:1px}

.hero{left:0;top:191px;width:820px;height:490px}
.hero-photo{left:0;top:0;width:356px;height:490px;background:linear-gradient(160deg,#e6ecf2 0%,#c9d3de 45%,#2c3e5a 75%,#1f2c44 100%)}
.hero-panel{left:356px;top:0;width:464px;height:490px;background:linear-gradient(180deg,#4ea7e8,#489fe2);text-align:center;color:var(--white)}
.hero-panel .lead{position:absolute;left:0;width:464px;font-size:22px}
.hero-panel .headline{position:absolute;left:0;width:464px;font-size:42px;font-weight:700;color:var(--ink);line-height:49px}
.hero-panel .years{position:absolute;left:0;width:464px;font-size:58px;font-weight:700}
.hero-panel .exp{font-weight:700;text-decoration:underline;text-underline-offset:4px}
.btn-learn{position:absolute;left:145px;top:382px;width:175px;height:54px;border-radius:27px;background:var(--white);color:var(--btn-blue);font-weight:700;font-size:18px;line-height:54px;text-align:center}

.intro{left:0;top:702px;width:820px;text-align:center;font-size:20px;line-height:37px;color:var(--ink-soft)}
.partners{left:0;top:809px;width:820px;height:85px}

.services{left:0;top:941px;width:820px;height:544px;background:var(--band)}
.services h2{position:absolute;left:0;top:30px;width:820px;text-align:center;font-size:29px;font-weight:700;color:var(--blue)}
.service{position:absolute;display:flex;align-items:center;gap:18px;font-size:21px;color:var(--ink);line-height:26px}
.service svg{flex:none}

.location{left:0;top:1485px;width:820px;height:502px}
.map{left:24px;top:49px;width:417px;height:407px;border-radius:34px;background:linear-gradient(135deg,#eceae4,#e2e1da 60%,#d8dcc8)}
.loc-text{left:479px;top:88px;font-family:"Arimo",Arial,sans-serif;color:var(--ink)}
.loc-text h3{font-size:37px;font-weight:700;margin-bottom:18px}
.loc-text p{font-size:20px;line-height:38px;letter-spacing:.3px}
.loc-text .contact{margin-top:14px}
.btn-contact{left:479px;top:392px;width:178px;height:53px;border-radius:27px;background:var(--btn-blue);color:var(--white);font-family:"Arimo",Arial,sans-serif;font-weight:700;font-size:20px;line-height:53px;text-align:center}

.footer{left:0;top:1987px;width:820px;height:137px;background:var(--footer);color:var(--white);font-size:20px}
.footer .copy{position:absolute;left:23px;top:54px}
.footer .unsub{position:absolute;right:28px;top:54px}
</style>
</head>
<body>

<h1 class="abs board-title">EMAIL NEWLETTER DESIGN IDEA</h1>
<div class="abs board-brand"><div class="name">Velto</div><div class="sub">network services</div></div>
<ul class="abs features">
  <li>Responsive Template ( PC, Mobiles etc)</li>
  <li>Width : 600px</li>
  <li>Easily editable colors, text</li>
  <li>Content placement easily changeable</li>
</ul>

<main class="abs email">
  <div class="abs email-brand"><div class="name">Velto</div><div class="sub">network services</div></div>

  <section class="abs hero">
    <div class="abs hero-photo" role="img" aria-label="Photo of a smiling executive in a suit with arms crossed in a bright office"></div>
    <div class="abs hero-panel">
      <div class="lead" style="top:52px">We are the best</div>
      <div class="headline" style="top:88px">Managed IT<br>Service Providers</div>
      <div class="lead" style="top:194px">in the industry with a</div>
      <div class="lead" style="top:239px"><span class="exp">business experience</span> of</div>
      <div class="years" style="top:271px">28 years</div>
      <div class="btn-learn">Learn More</div>
    </div>
  </section>

  <p class="abs intro">Over the years, we have branched out to become a leading IT Service provider<br>with a team of dedicated technicians.</p>

  <svg class="abs partners" width="820" height="85" viewBox="0 0 820 85" aria-label="Partner badges">
    <rect x="84" y="4" width="76" height="76" rx="4" fill="#eef3f7" stroke="#d5dbe0"/>
    <rect x="206" y="22" width="236" height="44" rx="4" fill="#e0262c"/>
    <circle cx="533" cy="42" r="35" fill="#1a8ad4"/>
    <rect x="635" y="18" width="90" height="48" rx="4" fill="#e4e4e4"/>
  </svg>

  <section class="abs services">
    <h2>OUR SERVICES</h2>
    <div class="service" style="left:47px;top:446px"></div>
  </section>

  <section class="abs location">
    <div class="abs map" role="img" aria-label="Street map with a red pin marking the office location"></div>
    <div class="abs loc-text">
      <h3>Our Location</h3>
      <p>418 North Carver Lane<br>Brookfield, MO, 65312 United<br>States</p>
      <p class="contact"><b>Call us :</b> 5550142871<br><b>Fax :</b> 5550149326</p>
    </div>
    <div class="abs btn-contact">Contact Us</div>
  </section>

  <footer class="abs footer">
    <span class="copy">Copyright © 2018 Velto Network Services</span>
    <span class="unsub">Unsubscribe</span>
  </footer>
</main>

<svg width="0" height="0" style="position:absolute">
  <defs>
    <symbol id="tick" viewBox="0 0 54 54">
      <circle cx="27" cy="27" r="24" fill="none" stroke="#2f8fde" stroke-width="4"/>
      <circle cx="27" cy="27" r="17" fill="#2f8fde"/>
      <path d="M18 27l7 7 16-17" fill="none" stroke="#ffffff" stroke-width="5" stroke-linecap="round" stroke-linejoin="round"/>
    </symbol>
  </defs>
</svg>

<div class="abs" style="left:185px;top:1269px;width:820px;height:544px">
  <div class="service" style="left:47px;top:118px"><svg width="54" height="54"><use href="#tick"/></svg>Proactive Ticketing</div>
  <div class="service" style="left:419px;top:105px"><svg width="54" height="54"><use href="#tick"/></svg>Server and Workstation<br>Monitoring</div>
  <div class="service" style="left:47px;top:200px"><svg width="54" height="54"><use href="#tick"/></svg>Help desk support</div>
  <div class="service" style="left:419px;top:200px"><svg width="54" height="54"><use href="#tick"/></svg>Data Backup Monitoring</div>
  <div class="service" style="left:47px;top:283px"><svg width="54" height="54"><use href="#tick"/></svg>Spam Protection</div>
  <div class="service" style="left:419px;top:283px"><svg width="54" height="54"><use href="#tick"/></svg>Regular Reports</div>
  <div class="service" style="left:47px;top:369px"><svg width="54" height="54"><use href="#tick"/></svg>Deskflow 240</div>
  <div class="service" style="left:419px;top:369px"><svg width="54" height="54"><use href="#tick"/></svg>Telecom Services</div>
  <div class="service" style="left:47px;top:448px"><svg width="54" height="54"><use href="#tick"/></svg>ISP Management</div>
  <div class="service" style="left:419px;top:448px"><svg width="54" height="54"><use href="#tick"/></svg>Vendor Management</div>
</div>

</body>
</html>
```